Derek Mavlow Business card

Hey there, I’m hoping to have a business card designed. I’m in Real estate and just switched to a new Brokerage called: The Property Quarter

The back could just be the company name maybe or whatever looks good!

I’ve attached some logos of our company and some cards my buddy had done up.

On the card:
Derek Mavlow
derekmavlow@postnest.example
587-204-6618
derekmavlow-homes.example

Target Market(s)

Home buyers and sellers

Industry/Entity Type

Real Estate

Contact Information for Business Card

just looking for a cool and modern design with my picture on it. I like the idea of Black and red being used.

Requirements
Must have
• all the details provided. I'm open to anything. Just want a professional looking card.

```html
<!DOCTYPE html>
<html lang="en">
<head>
<meta charset="utf-8">
<title>Derek Mavlow – Business Card</title>
<link rel="stylesheet" href="https://fonts.googleapis.com/css2?family=Montserrat:wght@600;800&family=Roboto:wght@300;400&display=swap">
<style>
  :root {
    --brand-red: #d0153a;
    --brand-red-deep: #a80f2d;
    --ink: #1d1d1f;
    --text-grey: #55565a;
    --paper: #ffffff;
    --stage: #e9e9eb;
    --photo-light: #f2f2f2;
    --photo-dark: #2b2f36;
  }
  * { box-sizing: border-box; margin: 0; padding: 0; }
  html, body {
    width: 1200px; height: 852px; overflow: hidden;
    background: var(--stage);
  }
  .sheet {
    width: 1200px; height: 852px;
    display: flex; align-items: center; justify-content: center; gap: 40px;
  }
  .card {
    width: 540px; height: 309px;
    border-radius: 26px;
    position: relative; overflow: hidden;
    box-shadow: 0 10px 28px rgba(0,0,0,.18);
  }

  /* Back */
  .card--back { background: var(--brand-red); }
  .card--back .pattern {
    position: absolute; inset: 0;
    background: linear-gradient(135deg, #c8102f 0%, var(--brand-red) 45%, var(--brand-red-deep) 100%);
  }
  .card--back .brand-name {
    position: absolute; right: 36px; bottom: 118px;
    font-family: "Montserrat", sans-serif; font-weight: 800;
    font-size: 22px; color: var(--paper); letter-spacing: .5px;
    text-transform: uppercase; line-height: 1.05; text-align: left;
  }

  /* Front */
  .card--front {
    background: var(--paper);
    border-bottom: 4px solid var(--brand-red);
  }
  .card--front .portrait {
    position: absolute; right: 0; top: 0;
    width: 230px; height: 305px;
    background: linear-gradient(180deg, var(--photo-light) 0%, #d9d4cf 30%, var(--photo-dark) 70%, #1f2227 100%);
  }
  .card--front .brand-name {
    position: absolute; left: 30px; top: 62px;
    font-family: "Montserrat", sans-serif; font-weight: 800;
    font-size: 34px; line-height: 1; color: var(--ink);
    text-transform: uppercase; letter-spacing: -.5px;
  }
  .card--front .accent-tab {
    position: absolute; left: 0; top: 196px;
    width: 12px; height: 26px; background: var(--brand-red);
  }
  .card--front .person-name {
    position: absolute; left: 30px; top: 194px;
    font-family: "Montserrat", sans-serif; font-weight: 600;
    font-size: 20px; color: var(--brand-red);
  }
  .contact-list {
    position: absolute; left: 30px; top: 232px;
    list-style: none;
    font-family: "Roboto", sans-serif; font-weight: 300;
    font-size: 12.5px; color: var(--text-grey);
  }
  .contact-list li {
    display: flex; align-items: center; gap: 7px;
    height: 18px;
  }
  .contact-list svg { width: 11px; height: 11px; flex: none; }
</style>
</head>
<body>
<main class="sheet">

  <section class="card card--back" aria-label="Card back">
    <div class="pattern" role="img" aria-label="Embossed repeating brokerage name pattern in tonal red"></div>
    <p class="brand-name">The Property<br>Quarter</p>
  </section>

  <section class="card card--front" aria-label="Card front">
    <div class="portrait" role="img" aria-label="Portrait photo of Derek Mavlow in a dark blazer and white shirt"></div>
    <p class="brand-name">The Property<br>Quarter</p>
    <span class="accent-tab"></span>
    <h1 class="person-name">Derek Mavlow</h1>
    <ul class="contact-list">
      <li>
        <svg viewBox="0 0 24 24"><path fill="#d0153a" d="M6.6 10.8a15.5 15.5 0 0 0 6.6 6.6l2.2-2.2a1 1 0 0 1 1-.25 11.4 11.4 0 0 0 3.6.57 1 1 0 0 1 1 1V20a1 1 0 0 1-1 1A17 17 0 0 1 3 4a1 1 0 0 1 1-1h3.5a1 1 0 0 1 1 1c0 1.25.2 2.45.57 3.57a1 1 0 0 1-.25 1z"/></svg>
        587-204-6618
      </li>
      <li>
        <svg viewBox="0 0 24 24"><path fill="#d0153a" d="M3 5h18a1 1 0 0 1 1 1v12a1 1 0 0 1-1 1H3a1 1 0 0 1-1-1V6a1 1 0 0 1 1-1zm9 7.2L4 7.4V8l8 4.8L20 8v-.6z"/></svg>
        derekmavlow@postnest.example
      </li>
      <li>
        <svg viewBox="0 0 24 24"><circle cx="12" cy="12" r="10" fill="#d0153a"/><path fill="none" stroke="#fff" stroke-width="1.5" d="M2 12h20M12 2c3 3 3 17 0 20M12 2c-3 3-3 17 0 20"/></svg>
        derekmavlow-homes.example
      </li>
    </ul>
  </section>

</main>
</body>
</html>
```